Letterhead, stationery and email signature for construction business

I need the letterhead, stationery and email signature designs for a construction business. I want them to have a corporate feel to them.

I've attached the logo for reference.

```html
<!DOCTYPE html>
<html lang="en">
<head>
<meta charset="utf-8">
<title>Norvale Builders – Business Card</title>
<link href="https://fonts.googleapis.com/css2?family=Montserrat:wght@700&family=Roboto:wght@400&display=swap" rel="stylesheet">
<style>
  :root {
    --bg: #9c9c9c;
    --card: #f4f4f3;
    --brand-blue: #3a5faa;
    --deep-blue: #1f45a4;
    --ink: #5b5b61;
    --rule: #66666c;
  }
  * { margin: 0; padding: 0; box-sizing: border-box; }
  html, body {
    width: 1200px; height: 1013px; overflow: hidden;
    background: var(--bg);
  }
  .canvas {
    position: relative; width: 1200px; height: 1013px;
  }
  .card {
    position: absolute; left: 250px; width: 700px; height: 400px;
    box-shadow: 0 10px 28px rgba(0,0,0,.25);
  }
  .card--front { top: 80px; background: var(--card); }
  .card--back { top: 533px; background: var(--deep-blue); }

  .brand {
    position: absolute; right: 56px; top: 56px;
    display: flex; align-items: center; gap: 14px;
  }
  .brand__square { width: 54px; height: 54px; background: var(--ink); }
  .brand__name {
    font-family: "Montserrat", sans-serif; font-weight: 700;
    color: var(--brand-blue); font-size: 30px; line-height: 1.05;
    letter-spacing: .5px;
  }

  .person { position: absolute; left: 56px; top: 150px; }
  .person__name {
    font-family: "Montserrat", sans-serif; font-weight: 700;
    color: var(--brand-blue); font-size: 22px; letter-spacing: .3px;
  }
  .person__title {
    font-family: "Roboto", sans-serif; color: var(--ink);
    font-size: 17px; margin-top: 2px;
  }
  .rule {
    position: absolute; left: 200px; right: 56px; top: 196px;
    height: 1px; background: var(--rule);
  }
  .contacts {
    position: absolute; left: 56px; top: 214px; list-style: none;
    font-family: "Roboto", sans-serif; color: var(--ink); font-size: 17px;
  }
  .contacts li { display: flex; align-items: center; gap: 10px; height: 27px; }
  .contacts svg { width: 17px; height: 17px; flex: none; }

  .address {
    position: absolute; right: 56px; bottom: 52px; text-align: right;
    font-family: "Roboto", sans-serif; color: var(--ink);
    font-size: 17px; line-height: 1.4;
  }

  .card__pattern { position: absolute; inset: 0; background: linear-gradient(160deg, #3553b0, #2a4aa6 55%, #5f74bd); }
</style>
</head>
<body>
<main class="canvas">
  <section class="card card--front">
    <div class="brand">
      <span class="brand__square"></span>
      <span class="brand__name">NORVALE<br>BUILDERS</span>
    </div>

    <div class="person">
      <p class="person__name">DANIEL R. WHITFORD</p>
      <p class="person__title">Founder &amp; CEO</p>
    </div>
    <div class="rule"></div>

    <ul class="contacts">
      <li>
        <svg viewBox="0 0 24 24" fill="var(--brand-blue)"><path d="M6.6 10.8a15.1 15.1 0 0 0 6.6 6.6l2.2-2.2c.3-.3.7-.4 1-.2 1.1.4 2.3.6 3.6.6.6 0 1 .4 1 1V20c0 .6-.4 1-1 1A17 17 0 0 1 3 4c0-.6.4-1 1-1h3.5c.6 0 1 .4 1 1 0 1.2.2 2.4.6 3.6.1.3 0 .7-.2 1z"/></svg>
        (555)210-4836
      </li>
      <li>
        <svg viewBox="0 0 24 24" fill="none" stroke="var(--brand-blue)" stroke-width="2"><rect x="2" y="5" width="20" height="14"/><path d="M2 5l10 8 10-8"/></svg>
        hello@norvale.com
      </li>
      <li>
        <svg viewBox="0 0 24 24" fill="none" stroke="var(--brand-blue)" stroke-width="1.6"><circle cx="12" cy="12" r="10"/><ellipse cx="12" cy="12" rx="4.5" ry="10"/><path d="M2 12h20M4 7h16M4 17h16"/></svg>
        www.norvale.com
      </li>
    </ul>

    <address class="address" style="font-style:normal">
      Norvale Builders, Ltd.<br>
      2470 Harbor Ridge Road<br>
      Lakeview, CA 90000
    </address>
  </section>

  <section class="card card--back">
    <div class="card__pattern" role="img" aria-label="Embossed repeating brand-mark pattern in tonal blues"></div>
  </section>
</main>
</body>
</html>
```